2 sided postcard for New Internet Customers

We would like a design for a two sided postcard (with room for mailing label), dimensions 9 1/4 by 6 1/4 to be sent via US Mail.

The postcard needs to include our logo (attached) and the text
Fiber Optic Internet
888-219-6083
http://www.brightwave.com
Speeds up to 1 Gig, with packages starting at $55

These will be sent to people who do not have our service.

Since this is going to be "junk mail" we probably only have 1 second or less to capture someone's attention to encourage them to read the entire postcard.

We are a "mom and pop" telecommunications company that provides internet, phone, and television services on the fiber optic network that we designed, built, and maintain.

We started as a dial up ISP in 1995, and have extraordinary technical support based in Freeport PA, our customers actually get the speeds they pay for, and our service is highly reliable.

We have a slogan (which you can choose to use or ignore) which is
"I Got Wired with Bramhollow"

Existing customers can earn a $50 credit for every new customer they refer to us. Unlike most large cable and internet companies we have very happy customers... some who have stayed with us for decades.

I've attached our previous postcard, which I really dislike. It does have a blank spot for where the mailing label should go.

Target Market(s)

New Internet Customers in Western Pennsylvania

Industry/Entity Type

Internet

Font styles to use
Other font styles liked:
• Just match our logo.

Colors

Designer to choose colors to be used in the design.

Requirements
Must have
• The postcard needs to include our logo, and the text Fiber Optic Internet 888-219-6083 http://www.brightwave.com Speeds up to 1 Gig, with packages starting at $55
Nice to have
• The colors and fonts should look good with our logo.
Should not have
• Should not have small print or lots of text. Both sides need to capture attention.

```html
<!DOCTYPE html>
<html lang="en">
<head>
<meta charset="utf-8">
<title>Bramhollow Fiber Optic Internet Postcard</title>
<link rel="stylesheet" href="https://fonts.googleapis.com/css2?family=Poppins:wght@400;500;600;700&display=swap">
<style>
  :root {
    --brand-blue: #0a6cc0;
    --panel-blue: #5b8ac6;
    --fiber-light: #8fc3f0;
    --fiber-deep: #3f6fb6;
    --overlay-blue: #1f62b8;
    --ink: #222222;
    --paper: #ffffff;
    --backdrop: #f1f1f1;
  }
  * { margin: 0; padding: 0; box-sizing: border-box; }
  html, body {
    width: 1200px; height: 1200px; overflow: hidden;
    background: var(--backdrop);
    font-family: "Poppins", sans-serif;
  }
  .postcard {
    position: absolute; left: 57px; top: 351px;
    width: 1085px; height: 499px;
    background: var(--paper); overflow: hidden;
  }
  .postcard-shapes { position: absolute; inset: 0; width: 1085px; height: 499px; }
  .headline {
    position: absolute; left: 390px; top: 146px;
    color: var(--paper); font-weight: 700; line-height: 1;
  }
  .headline span { display: block; }
  .headline .line-big { font-size: 60px; letter-spacing: -1px; margin-bottom: 6px; }
  .headline .line-small { font-size: 38px; font-weight: 600; margin-top: 6px; }
  .speed-offer {
    position: absolute; left: 705px; top: 244px; width: 200px;
    text-align: center; color: var(--ink); font-size: 21px; line-height: 1.25;
  }
  .speed-offer .speed-value { display: block; color: var(--brand-blue); font-size: 32px; font-weight: 700; line-height: 1.1; }
  .price {
    position: absolute; left: 882px; top: 362px; width: 180px;
    text-align: center; color: var(--paper);
  }
  .price .price-lead { font-size: 21px; display: block; }
  .price .price-value { font-size: 56px; font-weight: 700; line-height: 1.1; display: block; }
  .brand {
    position: absolute; left: 752px; top: 44px;
    display: flex; align-items: center; gap: 14px;
  }
  .brand-dot { width: 76px; height: 76px; border-radius: 50%; background: var(--brand-blue); }
  .brand-name { font-size: 25px; color: var(--ink); line-height: 1.1; }
  .brand-url { font-size: 16px; color: var(--ink); display: block; }
  .contact {
    position: absolute; left: 390px; top: 446px;
    display: flex; align-items: center; gap: 22px;
    font-size: 18px; color: var(--ink);
  }
  .contact-item { display: flex; align-items: center; gap: 10px; }
  .contact-item svg { width: 20px; height: 20px; }
</style>
</head>
<body>
  <div class="postcard">
    <svg class="postcard-shapes" viewBox="0 0 868 399" preserveAspectRatio="none" aria-hidden="false">
      <defs>
        <linearGradient id="fiberGlow" x1="0" y1="0" x2="1" y2="1">
          <stop offset="0" stop-color="var(--fiber-light)"/>
          <stop offset="0.55" stop-color="#6a9bd6"/>
          <stop offset="1" stop-color="var(--fiber-deep)"/>
        </linearGradient>
      </defs>
      <rect class="photo-panel" x="0" y="0" width="295" height="399" fill="url(#fiberGlow)" role="img" aria-label="Photo of a bundle of glowing fiber optic strands fanning upward"/>
      <rect class="headline-overlay" x="177" y="100" width="118" height="199" fill="var(--overlay-blue)" opacity="0.85"/>
      <path class="headline-wave" fill="var(--brand-blue)"
        d="M295,100 H500 C560,100 595,118 582,148 C570,175 530,192 480,205 C520,212 545,232 560,262 C572,288 560,299 548,299 H295 Z"/>
      <path class="headline-streak" fill="var(--paper)"
        d="M432,246 C480,250 530,268 560,296 C525,272 480,258 432,252 Z"/>
      <path class="price-wave" fill="var(--brand-blue)"
        d="M700,150 C760,135 820,128 868,136 V399 H664 C642,340 690,292 742,272 C800,250 818,212 782,192 C752,176 722,166 700,150 Z"/>
    </svg>

    <div class="brand">
      <div class="brand-dot"></div>
      <div class="brand-name">Bramhollow, Inc.<span class="brand-url">www.bramhollow.com</span></div>
    </div>

    <h1 class="headline">
      <span class="line-big">Fiber</span>
      <span class="line-big">Optic</span>
      <span class="line-small">Internet</span>
    </h1>

    <p class="speed-offer">Speeds up to<span class="speed-value">1 GIG</span>with packages</p>

    <p class="price"><span class="price-lead">starting at</span><span class="price-value">$55</span></p>

    <div class="contact">
      <span class="contact-item">
        <svg viewBox="0 0 24 24" aria-hidden="true"><path fill="var(--ink)" d="M6.6 10.8a15.1 15.1 0 0 0 6.6 6.6l2.2-2.2a1 1 0 0 1 1-.25 11.4 11.4 0 0 0 3.6.6 1 1 0 0 1 1 1V20a1 1 0 0 1-1 1A17 17 0 0 1 3 4a1 1 0 0 1 1-1h3.5a1 1 0 0 1 1 1c0 1.25.2 2.45.6 3.6a1 1 0 0 1-.25 1z"/></svg>
        888-219-6083
      </span>
      <span class="contact-item">
        <svg viewBox="0 0 24 24" aria-hidden="true"><g fill="none" stroke="var(--ink)" stroke-width="1.8"><circle cx="12" cy="12" r="9"/><ellipse cx="12" cy="12" rx="4" ry="9"/><path d="M3 12h18M5 7h14M5 17h14"/></g></svg>
        www.brightwave.com
      </span>
    </div>
  </div>
</body>
</html>
```